LOS PINOS DE ARENA - EXCLUSIVE AND LUXURY REAL ESTATE PROJECT

Se trata del diseño de un mono poste grande (4 m x 2 m) o (8m x 3m) anunciando la construcción de 30 villas de lujo en un terreno en primera línea de playa en el sur de España (Cádiz).

La idea es crear expectación y transmitir lujo y exclusividad.

Target Market(s)

Clientes de alto poder adquisitivo que quieran adquirir su segunda vivienda en un entorno privilegiado a escasos pasos de una de las playas más bonitas de Cádiz.

Industry/Entity Type

REAL ESTATE

Colors

Designer to choose colors to be used in the design.

Requirements
Must have
• LOS PINOS DE ARENA as the name of the development
Nice to have
• Crear expectación con ideas del tipo: “Coming soon” o “No te lo puedes perder”

```html
<!DOCTYPE html>
<html lang="es">
<head>
<meta charset="utf-8">
<title>Los Pinos de Arena – Loading</title>
<link href="https://fonts.googleapis.com/css2?family=Nunito:wght@800;900&family=Roboto+Slab:wght@700&display=swap" rel="stylesheet">
<style>
  :root {
    --page-bg: #e9e9e9;
    --green-deep: #64973b;
    --green-light: #92c970;
    --fill-start: #b9e0a2;
    --fill-end: #86bd5e;
    --knob: #6faa48;
    --knob-dark: #4f8a2e;
    --pearl: #efe9ea;
    --pearl-shade: #d9d0d3;
    --white: #ffffff;
    --text-edge: #3f7424;
  }
  html, body {
    margin: 0;
    width: 1200px;
    height: 1200px;
    overflow: hidden;
    background: var(--page-bg);
  }
  .billboard {
    position: absolute;
    left: 40px;
    top: 320px;
    width: 1120px;
    height: 560px;
    background: radial-gradient(ellipse 48% 60% at 50% 48%, var(--green-light) 0%, var(--green-deep) 100%);
    overflow: hidden;
  }
  .headline {
    position: absolute;
    left: 0; right: 0;
    top: 42px;
    margin: 0;
    text-align: center;
    font-family: "Nunito", sans-serif;
    font-weight: 900;
    font-size: 88px;
    line-height: 1;
    letter-spacing: 1px;
    color: var(--pearl);
    -webkit-text-stroke: 2px var(--text-edge);
    paint-order: stroke fill;
    text-shadow: 2px 3px 0 var(--text-edge), 3px 5px 6px rgba(0,0,0,0.25);
  }
  .progress-frame {
    position: absolute;
    left: 108px;
    top: 148px;
    width: 902px;
    height: 210px;
    border-radius: 105px;
    background: linear-gradient(180deg, var(--white) 0%, var(--pearl) 55%, var(--pearl-shade) 100%);
    box-shadow: 0 8px 14px rgba(0,0,0,0.22), inset 0 -6px 10px rgba(0,0,0,0.08);
  }
  .progress-track {
    position: absolute;
    left: 77px;
    top: 88px;
    width: 745px;
    height: 83px;
    border-radius: 42px;
    background: linear-gradient(180deg, #d6cdd0 0%, var(--pearl) 60%);
    box-shadow: inset 0 4px 8px rgba(0,0,0,0.18);
  }
  .progress-fill {
    position: absolute;
    left: 0;
    top: 3px;
    width: 600px;
    height: 76px;
    border-radius: 38px;
    background: linear-gradient(90deg, var(--fill-start) 0%, var(--fill-end) 100%);
    box-shadow: inset 0 3px 4px rgba(255,255,255,0.5), inset 0 -4px 6px rgba(0,0,0,0.12);
  }
  .progress-knob {
    position: absolute;
    left: 611px;
    top: 79px;
    width: 181px;
    height: 101px;
    border-radius: 50px;
    background: linear-gradient(180deg, #8ec466 0%, var(--knob) 55%, var(--knob-dark) 100%);
    box-shadow: 0 6px 10px rgba(0,0,0,0.3), inset 0 3px 4px rgba(255,255,255,0.35);
    display: flex;
    align-items: center;
    justify-content: center;
    font-family: "Nunito", sans-serif;
    font-weight: 800;
    font-size: 44px;
    color: var(--pearl);
    text-shadow: 1px 2px 0 var(--text-edge), 2px 3px 4px rgba(0,0,0,0.3);
  }
  .project-name {
    position: absolute;
    left: 0; right: 0;
    top: 430px;
    margin: 0;
    text-align: center;
    font-family: "Roboto Slab", serif;
    font-weight: 700;
    font-size: 68px;
    line-height: 1;
    color: var(--white);
    text-shadow: 2px 3px 5px rgba(0,0,0,0.35);
  }
</style>
</head>
<body>
  <section class="billboard">
    <h1 class="headline">LOADING</h1>
    <div class="progress-frame" role="progressbar" aria-valuenow="95" aria-valuemin="0" aria-valuemax="100">
      <div class="progress-track">
        <div class="progress-fill"></div>
      </div>
      <div class="progress-knob">95%</div>
    </div>
    <h2 class="project-name">LOS PINOS DE ARENA</h2>
  </section>
</body>
</html>
```